New Law Firm needs a business card design

I need a business card for my new law firm called Tansey Wills and Probate. I would like designs to use my logo attached. My firm is new and modern. I like the colors orange, white, grey and black. The design I will chose will be one which uses color well, one which looks impressive, smart and modern.

Target Market(s)

Adults aged 30 to 50 seeking professional advice.

Industry/Entity Type

Law Firm

Requirements
Must have
• My logo which is attached.

Must have a modern font, similar to my logo and draft business card.
Should not have
• Any symbols about law, such as scales etc.

```html
<!DOCTYPE html>
<html lang="en">
<head>
<meta charset="utf-8">
<title>Tansey Wills and Probate – Business Card</title>
<link rel="stylesheet" href="https://fonts.googleapis.com/css2?family=Open+Sans:wght@300;400;700&display=swap">
<style>
  :root {
    --stage: #e9e8e6;
    --card-white: #fbfbfa;
    --card-grey-top: #6a6b6d;
    --card-grey-bottom: #4e4f51;
    --orange: #f0901e;
    --orange-light: #f7b45a;
    --text-grey: #6d6e70;
    --text-light: #f4f4f4;
    --brand-grey: #5f6062;
  }
  * { box-sizing: border-box; margin: 0; padding: 0; }
  html, body {
    width: 1200px; height: 800px; overflow: hidden;
    background: var(--stage);
    font-family: "Open Sans", Arial, sans-serif;
  }
  .stage {
    width: 1200px; height: 800px;
    display: flex; align-items: center; justify-content: center; gap: 40px;
  }
  .card {
    width: 540px; height: 310px; position: relative;
    border-radius: 3px;
    box-shadow: 0 10px 28px rgba(0,0,0,0.18);
    overflow: hidden;
  }

  /* Back */
  .card-back {
    background: linear-gradient(160deg, var(--card-grey-top), var(--card-grey-bottom));
    display: flex; align-items: center; justify-content: center;
  }
  .frame-ring {
    position: absolute; left: 50%; top: 50%;
    width: 286px; height: 286px; margin: -143px 0 0 -143px;
  }
  .contact-list {
    position: relative; list-style: none;
    display: flex; flex-direction: column; gap: 11px;
  }
  .contact-item {
    display: flex; align-items: center; gap: 10px;
    color: var(--text-light); font-size: 14px; font-weight: 400; letter-spacing: 0.2px;
  }
  .contact-icon {
    width: 18px; height: 18px; border-radius: 50%;
    background: var(--text-light);
    display: flex; align-items: center; justify-content: center; flex-shrink: 0;
  }
  .contact-icon svg { width: 11px; height: 11px; }

  /* Front */
  .card-front { background: var(--card-white); }
  .holder { position: absolute; left: 0; top: 40px; }
  .holder-name {
    display: flex; align-items: center; gap: 9px;
    color: var(--orange); font-weight: 700; font-size: 17px; letter-spacing: 0.4px;
  }
  .holder-name::before {
    content: ""; width: 20px; height: 18px; background: var(--orange);
  }
  .holder-role, .holder-quals {
    color: var(--text-grey); font-size: 11px; font-weight: 400; margin: 3px 0 0 29px;
  }
  .brand {
    position: absolute; right: 34px; top: 96px;
    display: flex; align-items: center; gap: 12px;
  }
  .brand-name {
    color: var(--brand-grey); font-weight: 400; font-size: 19px; line-height: 1.25; text-align: right;
  }
  .brand-dot {
    width: 14px; height: 14px; border-radius: 50%; background: var(--orange);
  }
  .address {
    position: absolute; right: 34px; bottom: 30px;
    color: var(--text-grey); font-size: 12px; font-style: normal; line-height: 1.5; text-align: left;
  }
</style>
</head>
<body>
<main class="stage">
  <section class="card card-back" aria-label="Business card back">
    <svg class="frame-ring" viewBox="0 0 286 286" aria-hidden="true">
      <defs>
        <linearGradient id="ring-tone" x1="0" y1="0" x2="1" y2="1">
          <stop offset="0" stop-color="#f7b45a"/>
          <stop offset="0.5" stop-color="#f0901e"/>
          <stop offset="1" stop-color="#c9731a"/>
        </linearGradient>
      </defs>
      <circle cx="143" cy="143" r="140" fill="none" stroke="url(#ring-tone)" stroke-width="3"/>
    </svg>
    <ul class="contact-list">
      <li class="contact-item">
        <span class="contact-icon">
          <svg viewBox="0 0 24 24"><path fill="#555" d="M6.6 10.8a15 15 0 0 0 6.6 6.6l2.2-2.2c.3-.3.7-.4 1-.2 1.1.4 2.3.6 3.6.6.6 0 1 .4 1 1V20c0 .6-.4 1-1 1A17 17 0 0 1 3 4c0-.6.4-1 1-1h3.5c.6 0 1 .4 1 1 0 1.3.2 2.5.6 3.6.1.3 0 .7-.2 1z"/></svg>
        </span>0412 300 118
      </li>
      <li class="contact-item">
        <span class="contact-icon">
          <svg viewBox="0 0 24 24"><rect x="7" y="2" width="10" height="20" rx="2" fill="#555"/><rect x="9" y="5" width="6" height="12" fill="#f4f4f4"/></svg>
        </span>0755 210 904
      </li>
      <li class="contact-item">
        <span class="contact-icon">
          <svg viewBox="0 0 24 24"><rect x="3" y="6" width="18" height="12" fill="#555"/><path d="M3 6l9 7 9-7" stroke="#f4f4f4" stroke-width="1.6" fill="none"/></svg>
        </span>daniel@tanseyprobate.com.au
      </li>
      <li class="contact-item">
        <span class="contact-icon">
          <svg viewBox="0 0 24 24" fill="none" stroke="#555" stroke-width="2"><circle cx="12" cy="12" r="9"/><ellipse cx="12" cy="12" rx="4" ry="9"/><path d="M3 12h18"/></svg>
        </span>www.tanseyprobate.com.au
      </li>
    </ul>
  </section>

  <section class="card card-front" aria-label="Business card front">
    <div class="holder">
      <h1 class="holder-name">DANIEL CARVER</h1>
      <p class="holder-role">Lawyer</p>
      <p class="holder-quals">Assoc.Deg.Law, BLJSt, LLB, Grad Dip Law.</p>
    </div>
    <div class="brand">
      <p class="brand-name">Tansey<br>Wills &amp; Probate</p>
      <span class="brand-dot" aria-hidden="true"></span>
    </div>
    <address class="address">8/214 Harlow Creek Rd<br>Harlow Creek Qld 4079</address>
  </section>
</main>
</body>
</html>
```